Plumbing Business Letterhead Design

Need a letterhead designed to use for my invoices and letters. I would like it to incorporate my business logo, which i will upload, and use light blue and grey colours. Or any colours that will work well with my logo (im not very good with art to know) . Also the letterhead needs to include the following:
Address - P.O Box 4862 Bega NSW 2550
Email - marcus@tfelwoodplumbing.com.au
ABN - 41 906 572 384
Licence No. - 582064K
Mobile - 0471286540

Plumbing

Sans Serif

```html
<!DOCTYPE html>
<html lang="en">
<head>
<meta charset="utf-8">
<title>Tfelwood Plumbing Letterhead</title>
<link href="https://fonts.googleapis.com/css2?family=Open+Sans:wght@400;600&family=Pinyon+Script&display=swap" rel="stylesheet">
<style>
  :root {
    --backdrop: #efefef;
    --paper: #ffffff;
    --ink: #5f5f5f;
    --ink-dark: #4a4a4c;
    --accent-blue: #2aa3dc;
  }
  * { box-sizing: border-box; margin: 0; padding: 0; }
  html, body {
    width: 1006px; height: 1200px; overflow: hidden;
    background: var(--backdrop);
    font-family: "Open Sans", Arial, sans-serif;
    color: var(--ink);
  }
  .letterhead {
    position: absolute;
    left: 189px; top: 187px;
    width: 622px; height: 819px;
    background: var(--paper);
  }
  .brand {
    position: absolute;
    left: 46px; top: 53px;
    display: flex; align-items: center; gap: 12px;
  }
  .brand-mark {
    width: 52px; height: 52px;
    background: var(--ink-dark);
  }
  .brand-name {
    font-size: 24px; font-weight: 600; line-height: 27px;
    color: var(--ink-dark);
  }
  .salutation {
    position: absolute; left: 46px; top: 222px;
    font-size: 18px; color: var(--ink-dark);
  }
  .letter-body {
    position: absolute; left: 46px; top: 272px; width: 531px;
    font-size: 11.6px; line-height: 16px; text-align: justify;
    hyphens: auto;
  }
  .letter-body p { margin-bottom: 16px; }
  .signature {
    position: absolute; left: 46px; top: 644px;
  }
  .signature-script {
    font-family: "Pinyon Script", cursive;
    font-size: 21px; color: var(--ink-dark); line-height: 26px;
  }
  .signature-name {
    font-size: 19px; color: var(--ink-dark); line-height: 26px;
  }
  .contact {
    position: absolute; left: 0; right: 0; top: 766px;
    text-align: center; font-size: 12px; line-height: 16px;
  }
  .contact .label { color: var(--accent-blue); }
  .contact .sep { margin: 0 5px; }
</style>
</head>
<body>
  <main class="letterhead">
    <header class="brand">
      <div class="brand-mark"></div>
      <div class="brand-name">Marcus Tfelwood<br>Plumbing</div>
    </header>

    <h1 class="salutation" style="font-weight:400">Dear Sir,</h1>

    <section class="letter-body">
      <p>Lorem Ipsum is simply dummy text of the printing and typesetting industry. Lorem Ipsum has been the industry's standard dummy text ever since the 1500s, when an unknown printer took a galley of type and scrambled it to make a type specimen book. It has survived not only five centuries, but also the leap into electronic typesetting, remaining essentially unchanged. It was popularised in the 1960s with the release of Letraset sheets containing Lorem Ipsum passages,</p>
      <p>and more recently with desktop publishing software like Aldus PageMaker including versions of Lorem Ipsum.Lorem Ipsum is simply dummy text of the printing and typesetting industry. Lorem Ipsum has been the industry's standard dummy text ever since the 1500s, when an unknown printer took a galley of type and scrambled it to make a type specimen book. It has survived not only five centuries, but also the leap into electronic typesetting, remaining essentially unchanged. It was popularised in the 1960s with the release of Letraset sheets containing Lorem Ipsum passages,</p>
      <p>and more recently with desktop publishing software like Aldus PageMaker including versions of Lorem Ipsum.he release of Letraset sheets containing Lorem Ipsum passages,he release of Letraset sheets containing Lorem Ipsum passages,</p>
      <p>Lorem Ipsum is simply dummy text of the printing and typesetting industry.Lorem Ipsum is simply dummy text of the printing and typesetting industry.Lorem Ipsum is simply dummy text of the printing and typesetting industry.</p>
    </section>

    <div class="signature">
      <div class="signature-script">Daniel Hartley</div>
      <div class="signature-name">Daniel Hartley</div>
    </div>

    <footer class="contact">
      <div><span class="label">Mobile -</span> 0471286540<span class="sep">|</span><span class="label">ABN -</span> 41 906 572 384<span class="sep">|</span><span class="label">Licence No. -</span> 582064K</div>
      <div><span class="label">Address -</span> P.O Box 4862 Bega NSW 2550<span class="sep">|</span><span class="label">Email -</span> marcus@tfelwoodplumbing.com.au</div>
    </footer>
  </main>
</body>
</html>
```